letterhead design using our existing logo

We are a small boutique property management business based in Sydney's Northern Beaches.
We are after a sleek, simple modern letterhead (A4) incorporating our logo and its colours.
Also matching envelope (DL)
I have attached the logo with black text and white text for design options.

Target Market(s)

29-69yo Male and Female

Industry/Entity Type

Property Management

Requirements
Must have
• - Keyhaven Estates logo
• - Address, number and website:
• Suite 7, 18-19 Harlow Parade, Brookvale NSW 2100
• Tel: Tom Carrick 0417 293 608 Lorena Adcock 0409 516 742 www.keyhavenestatesgroup.com.au
Nice to have
• sleek design that looks modern and professional
Should not have
• too many colours or too busy

```html
<!DOCTYPE html>
<html lang="en">
<head>
<meta charset="utf-8">
<title>Keyhaven Estates – Stationery</title>
<link rel="stylesheet" href="https://fonts.googleapis.com/css2?family=Open+Sans:wght@400;600&display=swap">
<style>
  :root {
    --backdrop: #e3e3e5;
    --paper: #ffffff;
    --ink: #141819;
    --teal: #177b8c;
    --text: #1b1b1b;
  }
  * { margin: 0; padding: 0; box-sizing: border-box; }
  html, body { width: 1189px; height: 1200px; overflow: hidden; }
  body {
    background: var(--backdrop);
    font-family: "Open Sans", Arial, sans-serif;
    position: relative;
    color: var(--text);
  }
  .sheet { position: absolute; overflow: hidden; }
  .brand-name {
    position: absolute;
    font-weight: 600;
    letter-spacing: -0.02em;
    white-space: nowrap;
    line-height: 1;
  }

  /* A4 letterhead */
  .letterhead {
    left: 50px; top: 99px; width: 507px; height: 657px;
    background: var(--paper);
  }
  .letterhead .brand-name { left: 16px; top: 60px; font-size: 27px; color: var(--ink); }
  .contact-block {
    position: absolute; right: 17px; top: 39px;
    text-align: right; font-size: 9.5px; line-height: 11.8px;
  }
  .contact-line { display: flex; justify-content: flex-end; align-items: center; gap: 4px; }
  .contact-name { color: var(--teal); }
  .contact-icon { width: 9px; height: 9px; flex: none; }
  .postal-address { margin-top: 6px; padding-right: 0; line-height: 11px; }

  .foot-bands { position: absolute; left: 0; bottom: 0; }

  /* Folder cover */
  .cover {
    left: 629px; top: 100px; width: 506px; height: 654px;
    background: var(--ink);
  }
  .cover .brand-name {
    left: 0; right: 0; top: 312px; text-align: center;
    font-size: 31px; color: var(--paper);
  }

  /* Compliments slip */
  .slip {
    left: 102px; top: 856px; width: 401px; height: 201px;
    background: var(--paper);
  }
  .slip .brand-name { left: 15px; top: 40px; font-size: 17px; color: var(--ink); }
  .slip-address {
    position: absolute; left: 16px; top: 158px;
    font-size: 6.5px; line-height: 8px;
  }

  /* DL envelope */
  .envelope {
    left: 681px; top: 856px; width: 403px; height: 201px;
    background: var(--ink);
  }
  .envelope-flap { position: absolute; left: 0; top: 0; }
  .envelope .brand-name {
    left: 0; right: 0; top: 21px; text-align: center;
    font-size: 10.5px; color: var(--ink);
  }
</style>
</head>
<body>

  <section class="sheet letterhead" aria-label="Letterhead">
    <div class="brand-name">KEYHAVEN ESTATES</div>

    <address class="contact-block" style="font-style: normal;">
      <div class="contact-line">
        <span><span class="contact-name">Tom Carrick</span> 0417 293 608</span>
        <svg class="contact-icon" viewBox="0 0 10 10" aria-hidden="true">
          <circle cx="5" cy="5" r="5" fill="#177b8c"/>
          <path d="M2.6 4.4c0-1 1.1-1.5 2.4-1.5s2.4.5 2.4 1.5l-1 .3-.3-.7H4l-.3.7zM3.3 5.3h3.4l.4 2H2.9z" fill="#fff"/>
        </svg>
      </div>
      <div class="contact-line">
        <span><span class="contact-name">Lorena Adcock</span> 0409 516 742</span>
        <svg class="contact-icon" viewBox="0 0 10 10" aria-hidden="true">
          <circle cx="5" cy="5" r="5" fill="#177b8c"/>
          <path d="M2.6 4.4c0-1 1.1-1.5 2.4-1.5s2.4.5 2.4 1.5l-1 .3-.3-.7H4l-.3.7zM3.3 5.3h3.4l.4 2H2.9z" fill="#fff"/>
        </svg>
      </div>
      <div class="contact-line">
        <span>www.keyhavenestatesgroup.com.au</span>
        <svg class="contact-icon" viewBox="0 0 10 10" aria-hidden="true">
          <circle cx="5" cy="5" r="5" fill="#177b8c"/>
          <rect x="2.5" y="3.2" width="5" height="3.6" rx="0.4" fill="#fff"/>
          <path d="M2.6 3.4 5 5.3l2.4-1.9" fill="none" stroke="#177b8c" stroke-width="0.6"/>
        </svg>
      </div>
      <div class="postal-address">
        Suite 7, 18-19 Harlow Parade<br>Brookvale NSW 2100
      </div>
    </address>

    <svg class="foot-bands" width="507" height="19" viewBox="0 0 507 19" aria-hidden="true">
      <polygon points="0,7 318,7 313,19 0,19" fill="#141819"/>
      <polygon points="322,0 507,0 507,19 315,19" fill="#177b8c"/>
    </svg>
  </section>

  <section class="sheet cover" aria-label="Presentation folder cover">
    <div class="brand-name">KEYHAVEN ESTATES</div>
  </section>

  <section class="sheet slip" aria-label="Compliments slip">
    <div class="brand-name">KEYHAVEN ESTATES</div>
    <address class="slip-address" style="font-style: normal;">
      Suite 7, 18-19 Harlow Parade<br>Brookvale NSW 2100
    </address>
    <svg class="foot-bands" width="401" height="17" viewBox="0 0 401 17" aria-hidden="true">
      <polygon points="0,6 248,6 244,17 0,17" fill="#141819"/>
      <polygon points="253,0 401,0 401,17 246,17" fill="#177b8c"/>
    </svg>
  </section>

  <section class="sheet envelope" aria-label="DL envelope">
    <svg class="envelope-flap" width="403" height="57" viewBox="0 0 403 57" aria-hidden="true">
      <path d="M0 0H403L396 46Q394 56 384 56H19Q9 56 7 46Z" fill="#ffffff"/>
    </svg>
    <div class="brand-name">KEYHAVEN ESTATES</div>
  </section>

</body>
</html>
```